Legal Service Estimated Retainer and Average Case Value

We need an 11x14 flyer that contains the standard retainers and average cost be case, both provided in documents, for each case type we handle. We need the information displayed, preferably in a way that makes the information readable but less troubling to a client shocked at price of litigation. We need one sheet with the retainers and average case value merged into one table.

Target Market(s)

Potential Clients

Font styles to use
Serif
Sans Serif

```html
<!DOCTYPE html>
<html lang="en">
<head>
<meta charset="utf-8">
<title>Legal Service Estimated Retainer and Average Case Value</title>
<link href="https://fonts.googleapis.com/css2?family=Noticia+Text:wght@400;700&family=Nunito:wght@400;600&display=swap" rel="stylesheet">
<style>
  :root {
    --navy-top: #1f3a80;
    --navy-mid: #182a63;
    --navy-deep: #10173f;
    --royal: #0055a5;
    --navy-panel: #1e3372;
    --gold: #fdc15a;
    --ink: #161a2c;
    --row-alt: #e4ebf6;
    --row-white: #ffffff;
    --rule: #b9d3ee;
    --footer-light: #f2f3f6;
    --footer-shade: #e6e8ec;
    --brand: #1b2a5e;
  }
  * { box-sizing: border-box; margin: 0; padding: 0; }
  html, body { width: 990px; height: 1200px; overflow: hidden; background: #ffffff; }
  .flyer {
    position: relative;
    width: 990px;
    height: 1200px;
    overflow: hidden;
    background: linear-gradient(160deg, var(--navy-top) 0%, var(--navy-mid) 45%, var(--navy-deep) 80%);
    font-family: "Noticia Text", Georgia, serif;
  }
  .flyer-title {
    position: absolute;
    top: 50px;
    left: 0;
    width: 100%;
    text-align: center;
    color: #ffffff;
    font-weight: 400;
    font-size: 36px;
    line-height: 44px;
    letter-spacing: 0.3px;
  }
  .fee-table {
    position: absolute;
    top: 182px;
    left: 62px;
    width: 880px;
    border-collapse: collapse;
    table-layout: fixed;
  }
  .fee-table col.col-case { width: 418px; }
  .fee-table col.col-retainer { width: 222px; }
  .fee-table col.col-average { width: 240px; }
  .fee-table th {
    background: var(--gold);
    color: var(--ink);
    font-weight: 700;
    font-size: 20px;
    height: 56px;
    text-align: center;
    border-right: 1px solid #f5d79c;
  }
  .fee-table th.case-type { text-align: left; padding-left: 26px; }
  .fee-table th:last-child { border-right: none; }
  .fee-table td {
    height: 50px;
    color: var(--ink);
    border-right: 1px solid var(--rule);
    vertical-align: middle;
  }
  .fee-table td:last-child { border-right: none; }
  .fee-table tbody tr:nth-child(odd) td { background: var(--row-white); }
  .fee-table tbody tr:nth-child(even) td { background: var(--row-alt); }
  .fee-table tr.two-line td { height: 61px; }
  .fee-table td.case-name {
    padding-left: 27px;
    padding-right: 12px;
    font-size: 17px;
    line-height: 19px;
  }
  .fee-table td.amount {
    text-align: center;
    font-family: "Nunito", Arial, sans-serif;
    font-size: 16px;
  }
  .backdrop-shapes {
    position: absolute;
    top: 0; left: 0;
    width: 990px; height: 1200px;
  }
  .justice-figure {
    position: absolute;
    left: 740px;
    top: 932px;
    width: 245px;
    height: 160px;
    background: radial-gradient(ellipse at 60% 45%, rgba(60,90,170,0.55) 0%, rgba(40,64,140,0.3) 45%, rgba(30,51,114,0) 75%);
  }
  .brand {
    position: absolute;
    left: 52px;
    top: 1108px;
    color: var(--brand);
  }
  .brand-kicker {
    font-size: 13px;
    letter-spacing: 0.6px;
    line-height: 14px;
  }
  .brand-name {
    font-size: 29px;
    line-height: 32px;
    letter-spacing: 0.4px;
  }
  .contact-divider {
    position: absolute;
    left: 601px;
    top: 1078px;
    width: 1px;
    height: 103px;
    background: var(--brand);
  }
  .contact-list {
    position: absolute;
    left: 620px;
    top: 1080px;
    list-style: none;
    color: var(--ink);
    font-size: 14px;
    line-height: 17px;
  }
  .contact-list li {
    display: flex;
    align-items: flex-start;
    margin-bottom: 8px;
  }
  .contact-list li.address { margin-bottom: 12px; }
  .contact-icon {
    width: 12px;
    height: 12px;
    margin-right: 8px;
    margin-top: 2px;
    flex: none;
  }
</style>
</head>
<body>
<main class="flyer">
  <div class="justice-figure" role="img" aria-label="Faint statue of Lady Justice holding scales"></div>

  <svg class="backdrop-shapes" viewBox="0 0 990 1200" preserveAspectRatio="none" aria-hidden="true">
    <defs>
      <linearGradient id="footerFill" x1="0" y1="0" x2="1" y2="1">
        <stop offset="0" stop-color="#f6f7f9"/>
        <stop offset="1" stop-color="#e4e6ea"/>
      </linearGradient>
    </defs>
    <polygon class="panel-navy" points="355,993 990,835 990,1098" fill="#1e3372" opacity="0.55"/>
    <polygon class="panel-royal" points="0,935 355,993 0,1080" fill="#0055a5"/>
    <polygon class="panel-footer" points="0,1080 355,993 990,1100 990,1200 0,1200" fill="url(#footerFill)"/>
    <polygon class="accent-gold" points="355,991 990,1094 990,1102 355,996" fill="#fdc15a"/>
  </svg>

  <h1 class="flyer-title">Legal Service Estimated<br>Retainer and Average Case Value</h1>

  <table class="fee-table">
    <colgroup>
      <col class="col-case"><col class="col-retainer"><col class="col-average">
    </colgroup>
    <thead>
      <tr>
        <th class="case-type">Case Type</th>
        <th>Retainer Fee</th>
        <th>Average Fee</th>
      </tr>
    </thead>
    <tbody>
      <tr><td class="case-name">Divorce (3301 C)</td><td class="amount">$2,000</td><td class="amount">$1,500 - $3,000</td></tr>
      <tr><td class="case-name">Divorce (3301 D)</td><td class="amount">$2,500</td><td class="amount">$2,000 - $3,000</td></tr>
      <tr><td class="case-name">Divorce and Custody</td><td class="amount">$3,500</td><td class="amount">$5,000 - $8,000</td></tr>
      <tr><td class="case-name">Divorce and Equitable Distribution</td><td class="amount">$3,500</td><td class="amount">$6,000 - $10,000</td></tr>
      <tr><td class="case-name">Divorce and Support</td><td class="amount">$3,000</td><td class="amount">$2,000 - $4,000</td></tr>
      <tr><td class="case-name">Divorce, Custody and Support</td><td class="amount">$3,500</td><td class="amount">$8,000 - $12,000</td></tr>
      <tr class="two-line"><td class="case-name">Divorce, Equitable Distribution<br>and Support</td><td class="amount">$3,500</td><td class="amount">$8,000 - $12,000</td></tr>
      <tr class="two-line"><td class="case-name">Divorce, Equitable Distribution<br>and Custody</td><td class="amount">$5,000</td><td class="amount">$10,000 - $15,000</td></tr>
      <tr class="two-line"><td class="case-name">Divorce, Equitable Distribution,<br>Custody and Support</td><td class="amount">$3,500</td><td class="amount">$12,000 - $15,000</td></tr>
      <tr><td class="case-name">Custody Initial Order</td><td class="amount">$3,000</td><td class="amount">$4,000 - $7,000</td></tr>
      <tr><td class="case-name">Divorce, Custody and Support</td><td class="amount">$3,500</td><td class="amount">$5,000 - $8,000</td></tr>
      <tr><td class="case-name">Custody and Support</td><td class="amount">$3,000</td><td class="amount">$5,000 - $8,000</td></tr>
      <tr><td class="case-name">(PFA) Protection From Abuse</td><td class="amount">$2,000 Paid In Full</td><td class="amount">$1,500 - $3,000</td></tr>
    </tbody>
  </table>

  <div class="brand">
    <div class="brand-kicker">THE LAW OFFICE OF</div>
    <div class="brand-name">DANIEL M WHITFORD</div>
  </div>

  <div class="contact-divider"></div>
  <ul class="contact-list">
    <li class="phone">
      <svg class="contact-icon" viewBox="0 0 24 24" aria-hidden="true"><path fill="#1d4f9c" d="M6.6 10.8a15.1 15.1 0 0 0 6.6 6.6l2.2-2.2a1 1 0 0 1 1-.25 11.4 11.4 0 0 0 3.6.57 1 1 0 0 1 1 1V20a1 1 0 0 1-1 1A17 17 0 0 1 3 4a1 1 0 0 1 1-1h3.5a1 1 0 0 1 1 1c0 1.25.2 2.45.57 3.57a1 1 0 0 1-.25 1z"/></svg>
      <span>(555) 014-2290</span>
    </li>
    <li class="address">
      <svg class="contact-icon" viewBox="0 0 24 24" aria-hidden="true"><path fill="#1d4f9c" d="M12 2a7 7 0 0 0-7 7c0 5.25 7 13 7 13s7-7.75 7-13a7 7 0 0 0-7-7zm0 9.5A2.5 2.5 0 1 1 12 6.5a2.5 2.5 0 0 1 0 5z"/></svg>
      <span>1250 Fairmont Avenue<br>Suite 210, Millbrook, PA 17000</span>
    </li>
    <li class="web">
      <svg class="contact-icon" viewBox="0 0 24 24" aria-hidden="true"><g fill="none" stroke="#1d4f9c" stroke-width="2"><circle cx="12" cy="12" r="9.5"/><ellipse cx="12" cy="12" rx="4" ry="9.5"/><line x1="2.5" y1="12" x2="21.5" y2="12"/></g></svg>
      <span>www.whitfordlawoffice.com</span>
    </li>
  </ul>
</main>
</body>
</html>
```